The Gemstone Craft Studio Sales Business Card

The goal of this project is to create a interactive & effective business card design for SALES purposes with the intention to get customer on to our website and make a purchase or contact us about a product or service.
Website: WWW.RINGFORGEHUB.COM
GoogleMyBusiness: https://g.page/RingForgeHUB?gm
Facebook & Instagram: @THEGEMSTONECRAFTSTUDIO
Phone # & Text Message & Whatsapp Message: +1(555) 418-0293
Email: HELLO@RINGFORGEHUB.COM
Location: 4872 Brambleton Avenue Suite 512 Hollis Creek, NJ
(It would be necessary to have the appropriate ticker/icon for each social media platform as well as the location ticker and phone / messaging icons instead of spelling the words out.)
It is important to have the company logo and details but with an emphasis toward website. Feel free to also completely make one design your way and completely custom as you feel best.
The Gemstone Craft Studio is a Provider of Luxury Goods & Services such as: Custom Jewelry Design, Jewelry Repairs & Cleaning, Designer Jewelry, Luxury Gifts, 24 Karat Gold, 22 Karat Gold Jewelry, Diamond Jewelry, Insured Jewelry Appraisals, Loose Gemstones & Diamonds, Supporting Sustainability
Target Market(s)
People looking to invest in precious metals and gemstones as well as people looking to find a gift for a loved one for a special occasion. Customers looking to Custom Design Jewelry.
Contact Information for Business Card
Font styles to use
Other font styles liked:
- w.e you want
Colors
Designer to choose colors to be used in the design.
Requirements
Must have
- Website: WWW.RINGFORGEHUB.COM
- GoogleMyBusiness: https://g.page/RingForgeHUB?gm
- Facebook & Instagram: @THEGEMSTONECRAFTSTUDIO
- Phone # & Text Message & Whatsapp Message: +1(555) 418-0293
- Email: HELLO@RINGFORGEHUB.COM
- Location: 4872 Brambleton Avenue Suite 512 Hollis Creek, NJ
- (It would be necessary to have the appropriate ticker/icon for each social media platform as well as the location ticker and phone / messaging icons instead of spelling the words out.)
- It is important to have the company logo and details but with an emphasis toward website. Feel free to also completely make one design your way and completely custom as you feel best.
Nice to have
- The Gemstone Craft Studio is a Provider of Luxury Goods & Services such as: Custom Jewelry Design, Jewelry Repairs & Cleaning, Designer Jewelry, Luxury Gifts, 24 Karat Gold, 22 Karat Gold Jewelry, Diamond Jewelry, Insured Jewelry Appraisals, Loose Gemstones & Diamonds, Supporting Sustainability

```html
<!DOCTYPE html>
<html lang="en">
<head>
<meta charset="utf-8">
<title>The Gemstone Craft Studio — Business Card</title>
<link href="https://fonts.googleapis.com/css2?family=Open+Sans:wght@400;600;700&display=swap" rel="stylesheet">
<style>
  :root {
    --bg: #262626;
    --card: #1d1d1d;
    --red: #e31e2b;
    --gold: #f6c52a;
    --white: #f4f4f4;
  }
  * { box-sizing: border-box; margin: 0; padding: 0; }
  html, body { width: 1200px; height: 1021px; overflow: hidden; }
  body {
    background: var(--bg);
    font-family: "Open Sans", Arial, sans-serif;
    color: var(--white);
    position: relative;
  }
  .card {
    position: absolute;
    left: 190px;
    width: 820px;
    height: 469px;
    background: var(--card);
    box-shadow: 0 12px 30px rgba(0,0,0,.55);
    overflow: hidden;
  }
  .card--back { top: 36px; }
  .card--front { top: 528px; }

  /* brand name lockup */
  .brand { display: flex; align-items: center; gap: 18px; }
  .brand__mark { width: 46px; height: 46px; background: var(--red); flex: none; }
  .brand__name {
    color: var(--red);
    font-weight: 700;
    font-size: 34px;
    line-height: 1.1;
    text-transform: uppercase;
    letter-spacing: 1px;
    white-space: nowrap;
  }

  /* back: services */
  .services {
    position: absolute;
    left: 80px;
    top: 48px;
    list-style: none;
    font-size: 20px;
    line-height: 36px;
  }
  .services li::before {
    content: "•";
    color: var(--gold);
    margin-right: 8px;
  }
  .card--back .brand { position: absolute; left: 470px; top: 185px; }

  /* front: left column */
  .card--front .brand { position: absolute; left: 70px; top: 150px; }
  .links { position: absolute; left: 70px; top: 270px; font-size: 21px; line-height: 36px; }
  .link { display: flex; align-items: center; gap: 12px; white-space: nowrap; }
  .link--web { font-weight: 700; font-size: 24px; }
  .link--web .accent { color: var(--gold); }
  .icon { width: 20px; height: 20px; flex: none; }
  .accent-bar {
    position: absolute;
    left: 70px;
    bottom: 0;
    width: 340px;
    height: 16px;
    background: var(--gold);
  }

  /* front: right column */
  .contact { position: absolute; left: 460px; top: 150px; width: 340px; font-size: 19px; line-height: 32px; }
  .social-dot { width: 18px; height: 18px; background: var(--red); border-radius: 4px; flex: none; }
  .rule { height: 2px; background: var(--gold); margin: 14px 0; }
  .address { display: flex; gap: 12px; align-items: flex-start; white-space: nowrap; }
  .address .icon { margin-top: 6px; }
</style>
</head>
<body>

<section class="card card--back" aria-label="Card back">
  <ul class="services">
    <li>Custom Jewelry Design</li>
    <li>Jewelry Repairs &amp; Cleaning</li>
    <li>Designer Jewelry</li>
    <li>Luxury Gifts</li>
    <li>24 Karat Gold</li>
    <li>22 Karat Gold Jewelry</li>
    <li>Insured Jewelry Appraisals</li>
    <li>Diamond Jewelry</li>
    <li>Loose Gemstones &amp; Diamonds</li>
    <li>Supporting Sustainability</li>
  </ul>
  <div class="brand">
    <span class="brand__mark"></span>
    <span class="brand__name">The Gemstone<br>Craft Studio</span>
  </div>
</section>

<section class="card card--front" aria-label="Card front">
  <div class="brand">
    <span class="brand__mark"></span>
    <span class="brand__name">The Gemstone<br>Craft Studio</span>
  </div>

  <div class="links">
    <div class="link link--web">
      <svg class="icon" viewBox="0 0 20 20" fill="none" stroke="#e31e2b" stroke-width="1.6"><circle cx="10" cy="10" r="8"/><ellipse cx="10" cy="10" rx="3.5" ry="8"/><path d="M2 10h16M3.5 6h13M3.5 14h13"/></svg>
      <span>www.<span class="accent">ringforgehub</span>.com</span>
    </div>
    <div class="link">
      <svg class="icon" viewBox="0 0 20 20" fill="none" stroke="#e31e2b" stroke-width="1.6"><path d="M10 18s-6-6-6-10a6 6 0 0 1 12 0c0 4-6 10-6 10z"/><circle cx="10" cy="8" r="2.2"/></svg>
      <span>g.page/RingForgeHUB?gm</span>
    </div>
  </div>
  <div class="accent-bar"></div>

  <div class="contact">
    <div class="link"><span class="social-dot"></span><span>@thegemstonecraftstudio</span></div>
    <div class="link"><span class="social-dot"></span><span>@thegemstonecraftstudio</span></div>
    <div class="rule"></div>
    <div class="link">
      <svg class="icon" viewBox="0 0 20 20" fill="#e31e2b"><path d="M5 2l3 4-2 2c1 2.5 3.5 5 6 6l2-2 4 3-2 3C9 17 3 11 2 4z"/></svg>
      <span>+1(555) 418-0293</span>
    </div>
    <div class="link">
      <svg class="icon" viewBox="0 0 20 20" fill="none" stroke="#e31e2b" stroke-width="1.6"><rect x="2" y="4" width="16" height="12"/><path d="M2 4l8 7 8-7"/></svg>
      <span>hello@ringforgehub.com</span>
    </div>
    <div class="rule"></div>
    <div class="address">
      <svg class="icon" viewBox="0 0 20 20" fill="#e31e2b"><path d="M10 19s-6-6.5-6-11a6 6 0 0 1 12 0c0 4.5-6 11-6 11zm0-8.5a2.5 2.5 0 1 0 0-5 2.5 2.5 0 0 0 0 5z"/></svg>
      <span>4872 Brambleton Avenue, Suite 512<br>Hollis Creek, NJ</span>
    </div>
  </div>
</section>

</body>
</html>
```